Business Card & Word Docs from existing Logo

We need a business card with typical information plus layout to include electrical contractors license number, VORLE license and KMT license. We would like a word document layout for a proposal document, opening page with logo and design basic information; proposal to and proposal from and project name and number. Small basic single page letter for general documents. Email signature with logo.

We are an electrical, refrigeration and automation contractor. We work with reducing energy consumption for our customers and complex process solutions in electrical, refrigeration and automation.
Updates

Reason: Final changes/ revisions to designs.

Target Market(s)

Industrial and commercial businesses that require more than your average contractor.

Industry/Entity Type

Electrical

Requirements
Must have
• Propsal document must have a full opening page.

```html
<!DOCTYPE html>
<html lang="en">
<head>
<meta charset="utf-8">
<title>Frostvolt Contracting – Business Card</title>
<link rel="stylesheet" href="https://fonts.googleapis.com/css2?family=Arimo:wght@400;700&family=Source+Sans+3:wght@400;600&display=swap">
<style>
  :root {
    --brand-blue: #0a7db2;
    --brand-green: #1f9a3a;
    --navy: #0e2d52;
    --ink: #1c2433;
    --paper: #ffffff;
  }
  html, body {
    margin: 0;
    padding: 0;
    overflow: hidden;
    background: var(--paper);
  }
  .card {
    position: relative;
    width: 1200px;
    height: 703px;
    background: var(--paper);
    overflow: hidden;
    font-family: "Source Sans 3", Arial, sans-serif;
  }
  .brand-mark {
    position: absolute;
    left: 62px;
    top: 28px;
    width: 270px;
    height: 270px;
  }
  .brand-name {
    position: absolute;
    left: 390px;
    top: 36px;
    margin: 0;
    color: var(--brand-blue);
    font-family: "Source Sans 3", Arial, sans-serif;
    font-weight: 600;
    line-height: 1;
  }
  .brand-name .word {
    display: block;
    font-size: 104px;
    letter-spacing: -1px;
  }
  .brand-name .trade {
    display: block;
    margin-top: 26px;
    font-size: 56px;
    letter-spacing: 31px;
  }
  .rule {
    position: absolute;
    left: 41px;
    top: 321px;
    width: 1131px;
    height: 3px;
    background: var(--brand-green);
  }
  .person {
    position: absolute;
    right: 864px;
    top: 348px;
    text-align: right;
    font-family: "Arimo", Arial, sans-serif;
    color: var(--navy);
  }
  .person-name {
    margin: 0;
    font-size: 36px;
    font-weight: 700;
    line-height: 1.2;
    white-space: nowrap;
  }
  .person-role {
    margin: 8px 0 0;
    font-size: 36px;
    font-weight: 400;
    line-height: 1.2;
  }
  .contact {
    position: absolute;
    left: 402px;
    margin: 0;
    padding: 0;
    list-style: none;
    color: var(--ink);
    font-size: 24px;
    line-height: 34px;
  }
  .contact-phones { top: 357px; }
  .contact-web { top: 520px; }
  .contact .spaced { letter-spacing: 2px; }
  .licences {
    position: absolute;
    left: 12px;
    top: 648px;
    margin: 0;
    font-family: "Arimo", Arial, sans-serif;
    font-size: 31px;
    color: var(--navy);
    white-space: nowrap;
  }
</style>
</head>
<body>
  <main class="card">
    <svg class="brand-mark" viewBox="0 0 270 270" aria-hidden="true">
      <circle cx="135" cy="135" r="132" fill="var(--brand-green)"/>
    </svg>

    <h1 class="brand-name">
      <span class="word">FROSTVOLT</span>
      <span class="trade">CONTRACTING</span>
    </h1>

    <div class="rule"></div>

    <div class="person">
      <p class="person-name">Daniel Reeve</p>
      <p class="person-role">Director</p>
    </div>

    <ul class="contact contact-phones">
      <li>T: 07 5550 1820</li>
      <li>F: 07 5550 1820</li>
      <li>M : 0491 570 238</li>
    </ul>

    <ul class="contact contact-web">
      <li class="spaced">E: daniel@frostvolt.com.au</li>
      <li class="spaced">W : www.frostvolt.com.au</li>
      <li class="spaced">PO Box 2817, Cairns, Queensland, 4870</li>
    </ul>

    <p class="licences">Electrical Contractors License 40718,&nbsp; KMT 7305912,&nbsp; VORLE AA60294</p>
  </main>
</body>
</html>
```